Laboratory and geotechnical service provider needs Word template

We require a new Word Template for our business. We are looking for a modern, business-like format. We typically generate reports such as management plans, business plans, method statements, technical reports. These reports cover generally between 5 and 30 pages, but sometimes up to 500 pages including the appendices.

Lab reports have their own formats and are not parts of this scope.

Target Market(s)

We report to Clients such as construction industry contractors, governmental departments and engineering consultants.

Industry/Entity Type

Technical Service

Colors

Designer to choose colors to be used in the design.

Requirements
Must have
• The report needs a fancy cover page with a title field, subtitle, project field, client name field, reference number field. Photo/graphics as background on cover. Second page needs a revision table for document control. Table of contents up to 2 levels. Appendices to be part of TOC. Report first page with custom headings for body text, titles, subtitles, headings 1, 2, 3, etc. Include a table with caption, figure with caption, bullet list, numbered list. Appendix page. Please use fonts consistently, choose a common, but professional, modern font.
Nice to have
• We traditionally use black and yellow as company colours. Please visit our company page www.tarnvalecores.com.
Should not have
• The two attached word documents is what we use now for your information, we are looking for something better!

```html
<!DOCTYPE html>
<html lang="en">
<head>
<meta charset="utf-8">
<title>Tarnvale Cores Co. WLL — Report Template</title>
<link rel="stylesheet" href="https://fonts.googleapis.com/css2?family=Source+Sans+3:wght@300;400;700;900&display=swap">
<style>
:root{
  --yellow:#FFCF00;
  --backdrop:#FDCB1A;
  --black:#000;
  --dark:#4d4d4d;
  --paper:#fff;
  --ink:#3a3a3a;
}
*{margin:0;padding:0;box-sizing:border-box}
html,body{width:1200px;height:849px;overflow:hidden}
body{background:var(--backdrop);font-family:"Source Sans 3",sans-serif;color:var(--black);position:relative}
.brand{position:absolute;left:64px;top:20px;display:flex;align-items:center;gap:8px}
.brand-mark{width:54px;height:54px;border:2px solid var(--black)}
.brand-name{font-size:21px;font-weight:400}
.page{position:absolute;width:229px;height:324px;background:var(--paper);box-shadow:0 1px 3px rgba(0,0,0,.25);overflow:hidden}
.label{position:absolute;width:229px;text-align:center;font-size:12px}
.p-head{position:absolute;left:0;top:0;width:100%;height:27px;background:var(--yellow);border-bottom:1.2px solid var(--black)}
.p-head .mk{position:absolute;left:11px;top:11px;width:7px;height:7px;border:.8px solid var(--black)}
.p-head .nm{position:absolute;left:20px;top:11.5px;font-size:4.3px}
.p-head .ct{position:absolute;right:11px;top:10px;font-size:2.3px;line-height:1.6;text-align:right;color:var(--ink)}
.p-foot{position:absolute;left:0;top:305px;width:100%;height:1.5px;background:var(--yellow)}
.p-num{position:absolute;right:22px;top:310px;font-size:3.5px;color:var(--ink)}
.band{position:absolute;left:0;width:100%;height:9px;background:var(--yellow);font-size:4.5px;font-weight:700;padding:2.2px 22px}
.txt{position:absolute;left:22px;width:185px;font-size:3.6px;line-height:1.5;color:var(--ink)}
.txt p{margin-bottom:4px}
table{border-collapse:collapse;font-size:3.6px;color:var(--ink)}
.tbl{position:absolute;left:21px;width:186px}
.tbl th{background:var(--black);color:#fff;font-weight:400;text-align:left;padding:1.5px 2px}
.tbl td{padding:2.3px 2px}
.gray{background:var(--dark);color:#fff}
.cap{position:absolute;font-size:2.2px;font-style:italic;color:#777}
.photo{position:absolute;left:0;width:100%}
/* cover */
.cover-photo{top:0;height:324px;background:linear-gradient(160deg,#e8c431 0%,#b99a22 30%,#d8b52a 55%,#f1cc30 80%,#c9a523 100%)}
.cover-band{position:absolute;left:0;top:220px;width:100%;height:30px;background:rgba(60,60,60,.88)}
.cover-band .t{position:absolute;left:17px;top:4px;font-size:12.5px;font-weight:900;color:var(--yellow)}
.cover-band .s{position:absolute;left:17px;top:19px;font-size:6.2px;color:#fff}
.cover-band .b{position:absolute;right:11px;top:8px;font-size:5.5px;font-weight:700;color:var(--yellow)}
.cover-url{position:absolute;right:11px;top:251px;font-size:2.2px}
.cover .proj{position:absolute;left:17px;top:258px;font-size:10px;font-weight:700}
.cover .ref{position:absolute;left:17px;top:271px;font-size:3.6px}
.cover .cli{position:absolute;left:17px;top:290px;font-size:7.2px}
/* toc */
.toc{position:absolute;left:22px;top:53px;width:185px;font-size:3.6px;line-height:1.5;color:#666}
.toc div{display:flex;justify-content:space-between}
.toc .in{padding-left:14px}
.toc .gap{height:5.4px}
/* lists */
.list-h{font-weight:700;color:var(--black)}
.bul li{list-style:none;padding-left:14px;position:relative}
.bul li::before{content:"";position:absolute;left:7px;top:1.4px;width:2.3px;height:2.3px;background:var(--ink)}
/* side info */
.info{position:absolute;left:910px}
.info h2{font-size:21px;font-weight:700}
.font-l{font-size:16px;line-height:19px}
.swatch{position:absolute;top:704px;width:50px;height:50px;border:3px solid #fff}
.sw-label{position:absolute;top:759px;width:60px;text-align:center;font-size:11px;line-height:12.5px}
</style>
</head>
<body>

<div class="brand"><div class="brand-mark"></div><div class="brand-name">Tarnvale Cores Co. WLL</div></div>

<!-- 1 cover -->
<div class="page cover" style="left:64px;top:97px">
  <div class="photo cover-photo" role="img" aria-label="Yellow-toned photo of a lab technician at a microscope above a desert drilling rig"></div>
  <div class="cover-band"><div class="t">Document Title</div><div class="s">Document Subtitle</div><div class="b">Tarnvale Cores</div></div>
  <div class="cover-url">www.tarnvalecores.com</div>
  <div class="proj">Project Titlet</div>
  <div class="ref">Reference number</div>
  <div class="cli">Clients name</div>
</div>
<div class="label" style="left:64px;top:422px">Cover page</div>

<!-- 2 revision -->
<div class="page" style="left:346px;top:97px">
  <div class="p-head"><div class="mk"></div><div class="nm">Tarnvale Cores Co. WLL</div><div class="ct">+974 4000 1234<br>info@tarnvalecores.com<br>www.tarnvalecores.com</div></div>
  <table class="tbl" style="top:39px">
    <tr><th>Rev</th><th>Date</th><th>Details</th><th>Prepared</th><th>Checked</th><th>Approved</th></tr>
    <tr><td>1</td><td>03.12.2019</td><td>1st draft</td><td>RSV</td><td>TV</td><td>AJS</td></tr>
    <tr><td>2</td><td>04.12.2019</td><td>2nd draft</td><td>RSV</td><td>TV</td><td>AJS</td></tr>
    <tr><td>3</td><td>05.12.2019</td><td>1st Issue</td><td>RSV</td><td>TV</td><td>AJS</td></tr>
  </table>
  <div class="gray" style="position:absolute;left:130px;top:80px;width:77px;height:16px;font-size:3.6px;padding:1.5px 3px;line-height:2.1;border-top:.5px solid #fff">Copy no. : 1/5<br>Controlled Copy : &nbsp;YES</div>
  <div class="p-foot"></div><div class="p-num">2</div>
</div>
<div class="label" style="left:346px;top:422px">Revision list</div>

<!-- 3 toc -->
<div class="page" style="left:628px;top:97px">
  <div class="p-head"><div class="mk"></div><div class="nm">Tarnvale Cores Co. WLL</div><div class="ct">+974 4000 1234<br>info@tarnvalecores.com<br>www.tarnvalecores.com</div></div>
  <div class="band" style="top:34px">Table of contents</div>
  <div class="toc">
    <div><span>01 Introduction</span><span>03</span></div>
    <div><span>02 Project overview</span><span>04</span></div>
    <div class="in"><span>02.01 Under segment 1</span><span>04</span></div>
    <div class="in"><span>02.02 Under segment 2</span><span>05</span></div>
    <div class="in"><span>02.03 Under segment 3</span><span>06</span></div>
    <div><span>03 Technical requirements</span><span>08</span></div>
    <div class="in"><span>03.01 Under segment 1</span><span>11</span></div>
    <div class="in"><span>03.02 Under segment 2</span><span>13</span></div>
    <div class="in"><span>03.03 Under segment 3</span><span>15</span></div>
    <div class="in"><span>03.04 Under segment 4</span><span>18</span></div>
    <div class="in"><span>03.05 Under segment 5</span><span>23</span></div>
    <div class="in"><span>03.06 Under segment 6</span><span>29</span></div>
    <div><span>04 Business Management Requirement</span><span>32</span></div>
    <div class="in"><span>04.01 Under segment 1</span><span>31</span></div>
    <div class="in"><span>04.02 Under segment 2</span><span>38</span></div>
    <div class="in"><span>04.03 Under segment 3</span><span>41</span></div>
    <div class="gap"></div>
    <div><span>Appendix A</span><span>42</span></div>
    <div class="in"><span>Appendix A – Undersegment 1</span><span>43</span></div>
    <div><span>Appendix B</span><span>44</span></div>
    <div><span>Appendix C</span><span>48</span></div>
  </div>
  <div class="p-foot"></div><div class="p-num">3</div>
</div>
<div class="label" style="left:628px;top:422px">Table of contents</div>

<!-- 4 headings -->
<div class="page" style="left:910px;top:97px">
  <div class="p-head"><div class="mk"></div><div class="nm">Tarnvale Cores Co. WLL</div><div class="ct">+974 4000 1234<br>info@tarnvalecores.com<br>www.tarnvalecores.com</div></div>
  <div class="band" style="top:34px">1. Heading 1</div>
  <div class="txt" style="top:47px;font-size:4.3px;font-weight:700;color:var(--black)">1.1 Heading 2</div>
  <div class="txt" style="top:59px;font-size:4.3px">1.11 Heading 3</div>
  <div class="txt" style="top:71px;font-size:3.8px">Paragraph</div>
  <div class="txt" style="top:83px">At vero eos et accusamus et iusto odio dignissimos ducimus qui blanditiis praesentium voluptatum deleniti atque corrupti quos dolores et quas molestias excepturi sint occaecati cupiditate non provident, similique sunt in culpa qui officia deserunt mollitia animi, id est laborum et dolorum fuga. Et harum quidem rerum facilis est et expedita distinctio. Nam libero tempore, cum soluta nobis est eligendi optio cumque nihil impedit quo minus id quod maxime placeat facere possimus, omnis voluptas assumenda est, omnis dolor repellendus. Temporibus autem quibusdam et aut officiis debitis aut rerum necessitatibus saepe eveniet ut et voluptates repudiandae sint et molestiae non recusandae. Itaque earum rerum hic tenetur a sapiente delectus.</div>
  <table class="tbl" style="top:149px">
    <tr><th>No.</th><th>Title 1</th><th>Title 2</th><th>Title 3</th><th>Title 4</th></tr>
    <tr><td>1</td><td>Content</td><td>Content</td><td>Content</td><td>Content</td></tr>
    <tr><td>2</td><td>Content</td><td>Content</td><td>Content</td><td>Content</td></tr>
    <tr><td>3</td><td>Content</td><td>Content</td><td>Content</td><td>Content</td></tr>
    <tr class="gray"><td style="background:#fff"></td><td>Conclusion / Total / Sum</td><td></td><td>Pre Total</td><td style="font-weight:700">Total sum</td></tr>
  </table>
  <div class="gray" style="position:absolute;left:148px;top:192px;width:59px;height:7px;font-size:3.6px;font-weight:700;padding:1.5px 2px">Total sum</div>
  <div class="cap" style="left:22px;top:200px">Caption text for table style 1</div>
  <table style="position:absolute;left:21px;top:209px">
    <tr><td class="gray" style="width:56px;padding:1.8px 2px">List item 1</td><td style="padding:1.8px 4px">Text 01</td><td style="padding:1.8px 4px">01</td></tr>
    <tr><td class="gray" style="padding:1.8px 2px">List item 2</td><td style="padding:1.8px 4px">Text 02</td><td style="padding:1.8px 4px">02</td></tr>
    <tr><td class="gray" style="padding:1.8px 2px">List item 3</td><td style="padding:1.8px 4px">Text 03</td><td style="padding:1.8px 4px">03</td></tr>
    <tr><td class="gray" style="padding:1.8px 2px">List item 4</td><td style="padding:1.8px 4px">Text 04</td><td style="padding:1.8px 4px">04</td></tr>
    <tr><td class="gray" style="padding:1.8px 2px">List item 5</td><td style="padding:1.8px 4px">Text 05</td><td style="padding:1.8px 4px">05</td></tr>
  </table>
  <div style="position:absolute;left:77px;top:252px;width:47px;height:7px;background:var(--black);color:#fff;font-size:3.6px;font-weight:700;display:flex;justify-content:space-around;align-items:center"><span>Total</span><span>Value</span></div>
  <div class="cap" style="left:22px;top:261px">Caption text for table style 2</div>
  <div class="p-foot"></div><div class="p-num">4</div>
</div>
<div class="label" style="left:910px;top:422px">Headings + Paragraph + Tables</div>

<!-- 5 paragraph & image -->
<div class="page" style="left:64px;top:474px">
  <div class="p-head"><div class="mk"></div><div class="nm">Tarnvale Cores Co. WLL</div><div class="ct">+974 4000 1234<br>info@tarnvalecores.com<br>www.tarnvalecores.com</div></div>
  <div class="txt" style="top:34px"><p>Nam aliquet bibendum elit, ac imperdiet leo tristique sit amet. Pellentesque habitant morbi tristique senectus et netus et malesuada fames ac turpis egestas. Duis non scelerisque nunc. Donec luctus sollicitudin libero, eu condimentum ex tempor sit amet.</p><p>Vivamus a dapibus neque. Interdum et malesuada fames ac ante ipsum primis in faucibus. Fusce quis viverra ligula, a egestas elit. Integer ut luctus lacus. Nunc et pretium sem. Nulla varius lacus et ligula sollicitudin, vel tempor urna tincidunt. Nam et nulla pretium, rutrum mi nec, laoreet odio. Fusce scelerisque malesuada odio, et auctor enim lacinia vel. Sed ut varius lacus, vitae pulvinar metus.</p></div>
  <div class="photo" style="top:100px;height:128px;background:linear-gradient(180deg,#eef1f4 0%,#c9d0d8 45%,#8e99a6 100%)" role="img" aria-label="Photo of a bright laboratory hall with technicians in yellow coats at benches"></div>
  <div style="position:absolute;left:0;top:210px;width:100%;height:18px;background:rgba(50,50,50,.85);color:var(--yellow);font-size:6.3px;display:flex;align-items:center;justify-content:center">&#8592;&nbsp;Images if possible should always be from edge to edge.&nbsp;&#8594;</div>
  <div class="cap" style="left:22px;top:231px">Caption text for figure style 1</div>
  <div class="txt" style="top:240px">Sed ut perspiciatis unde omnis iste natus error sit voluptatem accusantium doloremque laudantium, totam rem aperiam, eaque ipsa quae ab illo inventore veritatis et quasi architecto beatae vitae dicta sunt explicabo. Nemo enim ipsam voluptatem quia voluptas sit aspernatur aut odit aut fugit, sed quia consequuntur magni dolores eos qui ratione voluptatem sequi nesciunt. Neque porro quisquam est, qui dolorem ipsum quia dolor sit amet, consectetur, adipisci velit, sed quia non numquam eius modi tempora incidunt ut labore et dolore magnam aliquam quaerat voluptatem. Ut enim ad minima veniam, quis nostrum exercitationem ullam corporis suscipit laboriosam.</div>
  <div class="p-foot"></div><div class="p-num">5</div>
</div>
<div class="label" style="left:64px;top:799px">Parapgraph &amp; Image</div>

<!-- 6 lists -->
<div class="page" style="left:346px;top:474px">
  <div class="p-head"><div class="mk"></div><div class="nm">Tarnvale Cores Co. WLL</div><div class="ct">+974 4000 1234<br>info@tarnvalecores.com<br>www.tarnvalecores.com</div></div>
  <div class="txt" style="top:34px"><p>Nullam fermentum, dolor quis iaculis maximus, sem erat auctor orci, a dignissim arcu nisi quis nunc. Sed eu sem at velit tempor finibus eget non felis. Vivamus lacus dolor, porta vitae orci vitae, auctor commodo nisl. Vestibulum luctus odio ex, nec pulvinar orci tincidunt at. Nam volutpat nisl at justo dignissim imperdiet.</p>
  <div class="list-h" style="margin-top:6px">List with munbers:</div>
  <div>01 Text enumeration<br>02 Text enumeration<br>03 Text enumeration<br>04 Text enumeration<br>05 Text enumeration<br>06 Text enumeration<br><span style="padding-left:14px">06.01 Subnumeration if needed</span><br><span style="padding-left:14px">06.02 Subnumeration if needed</span><br>07 Text enumeration<br>08 Text enumeration<br>09 Text enumeration<br>10 Text enumeration<br>11 Text enumeration<br>12 Text enumeration<br>13 Text enumeration<br>14 Text enumeration</div>
  <p style="margin-top:6px">Mauris et turpis molestie, tempus sem vel, pretium justo. Vivamus urna erat, pulvinar fringilla est ac, fringilla ullamcorper sem. Curabitur venenatis sit amet diam eu condimentum. Sed rutrum vehicula massa, dictum tristique nisl ultrices.</p>
  <div class="list-h" style="margin-top:5px">List with bullets:</div>
  <ul class="bul"><li>Bullet text</li><li>Bullet text</li><li>Bullet text</li><li>Bullet text</li><li>Bullet text</li><li>Bullet text</li><li>Bullet text</li><li>Bullet text</li><li>Bullet text</li></ul>
  <p style="margin-top:8px">Nunc in vulputate magna. Donec quis libero ut massa vulputate bibendum. Curabitur sodales, quam in vestibulum consectetur, ex neque varius elit, eget viverra nunc metus nec sem. Praesent semper nec magna dignissim tempor. Etiam vitae vehicula tellus. Nullam augue ligula, elementum non tellus ut, vestibulum imperdiet justo.</p></div>
  <div class="p-foot"></div><div class="p-num">6</div>
</div>
<div class="label" style="left:346px;top:799px">Numbered &amp; Bulleted lists</div>

<!-- 7 appendix -->
<div class="page" style="left:628px;top:474px">
  <div class="p-head"><div class="mk"></div><div class="nm">Tarnvale Cores Co. WLL</div><div class="ct">+974 4000 1234<br>info@tarnvalecores.com<br>www.tarnvalecores.com</div></div>
  <div class="band" style="top:34px">Appendix 1</div>
  <div class="txt" style="top:56px">Nemo enim ipsam voluptatem quia voluptas sit aspernatur aut odit aut fugit, sed quia consequuntur magni dolores eos qui ratione voluptatem sequi nesciunt. Neque porro quisquam est, qui dolorem ipsum quia dolor sit amet, consectetur, adipisci velit, sed quia non numquam eius modi tempora incidunt ut labore et dolore magnam aliquam quaerat voluptatem. Ut enim ad minima veniam, quis nostrum exercitationem ullam corporis suscipit laboriosam, nisi ut aliquid ex ea commodi consequatur?</div>
  <div class="p-foot"></div><div class="p-num">7</div>
</div>
<div class="label" style="left:628px;top:799px">Appendix page</div>

<!-- fonts & colours -->
<div class="info" style="top:540px"><h2>Fonts used :</h2></div>
<div class="info font-l" style="top:584px;font-weight:400">Corvel Sans - Regular</div>
<div class="info font-l" style="top:603px;font-weight:700">Corvel Sans - Bold</div>
<div class="info font-l" style="top:622px;font-weight:300">Corvel Sans - Light</div>
<div class="info" style="top:658px"><h2>Colors used :</h2></div>
<div class="swatch" style="left:910px;background:var(--black)"></div>
<div class="swatch" style="left:969px;background:var(--dark)"></div>
<div class="swatch" style="left:1028px;background:var(--yellow)"></div>
<div class="sw-label" style="left:905px">Black</div>
<div class="sw-label" style="left:959px;width:70px">Dark gray 1</div>
<div class="sw-label" style="left:1023px">Yellow<br>#FFCF00</div>

</body>
</html>
```